Moden - Costasol - Flower Shop

brisapetals is looking for a cool web design that has a airy, clean, mexicali feel to it.

See attached images and links for idea of what we mean with the above.

please no templates.

Target Market(s)

Local flower shop in San Diego, California

Industry/Entity Type

Shop

Requirements
Must have
• see. brisapetals.quartzcart.example - I did the site and logo...I love the logo - hate the site.

Going for this feel: http://www.velmorastudio.example/platebook/archives/tovarinos.php

I also attached another site I liked- I just feel like it may be to busy.

```html
<!DOCTYPE html>
<html lang="en">
<head>
<meta charset="utf-8">
<title>Brisa Petals — Costasol Spring Collection</title>
<link rel="stylesheet" href="https://fonts.googleapis.com/css2?family=Anonymous+Pro&family=Arvo:wght@400;700&family=Rokkitt:wght@200;900&family=Yellowtail&family=Damion&display=swap">
<style>
  :root {
    --header-bg: #3b3b3b;
    --nav-pink: #efc3d3;
    --logo-teal: #7fb2a8;
    --white: #ffffff;
    --hero-green: #2f4a2c;
    --mexi-yellow: #f3e36a;
    --button-cream: #f4efdf;
    --button-text: #555148;
    --chalk-dark: #2f2f2f;
    --chalk-mid: #4a4a4a;
    --card-caption: #f2f5f8;
    --card-text: #1f1f1f;
    --footer-text: #444444;
    --input-bg: #f1f1f1;
    --signup-red: #e0525f;
  }
  * { box-sizing: border-box; margin: 0; padding: 0; }
  html, body { width: 754px; height: 1200px; overflow: hidden; background: var(--white); }
  .page { position: relative; width: 754px; height: 1200px; overflow: hidden; }

  .site-header { position: absolute; left: 0; top: 0; width: 754px; height: 57px; background: var(--header-bg); }
  .site-header::after { content: ""; position: absolute; left: 0; top: 48px; width: 100%; height: 3px; background: var(--white); }
  .nav { position: absolute; top: 16px; display: flex; gap: 20px; font-family: "Arvo", serif; font-weight: 700; font-size: 15px; color: var(--nav-pink); }
  .nav-left { left: 53px; }
  .nav-right { right: 24px; gap: 24px; }

  .brand { position: absolute; left: 216px; top: 3px; width: 290px; height: 62px; background: var(--white); display: flex; align-items: center; justify-content: center; gap: 12px; z-index: 2; }
  .brand-name { font-family: "Arvo", serif; font-weight: 400; font-size: 22px; letter-spacing: 6px; color: var(--logo-teal); }
  .brand-dot { width: 18px; height: 18px; border-radius: 50%; background: var(--logo-teal); }

  .hero { position: absolute; left: 0; top: 51px; width: 754px; height: 362px; }
  .hero-photo { position: absolute; inset: 0; background:
      radial-gradient(circle at 12% 20%, rgba(200,40,60,.75), transparent 22%),
      radial-gradient(circle at 85% 25%, rgba(210,50,90,.7), transparent 20%),
      radial-gradient(circle at 50% 85%, rgba(190,35,55,.6), transparent 25%),
      linear-gradient(160deg, #3c5a36, var(--hero-green) 55%, #5a2a30); filter: brightness(.8); }
  .hero-emblem { position: absolute; left: 339px; top: 27px; width: 82px; height: 97px; border-radius: 40px 40px 30px 30px; background: rgba(255,255,255,.16); }
  .hero-title { position: absolute; left: 0; width: 754px; top: 128px; text-align: center; font-family: "Rokkitt", serif; font-size: 112px; line-height: 1; letter-spacing: 9px; color: var(--mexi-yellow); white-space: nowrap; }
  .hero-title .bold { font-weight: 900; }
  .hero-title .thin { font-weight: 200; }
  .hero-tagline { position: absolute; left: 0; width: 754px; top: 218px; text-align: center; font-family: "Yellowtail", "Damion", cursive; font-size: 40px; line-height: 1.1; color: var(--white); }
  .hero-button { position: absolute; left: 320px; top: 290px; width: 136px; height: 31px; background: var(--button-cream); font-family: "Anonymous Pro", monospace; font-size: 14px; letter-spacing: 2px; color: var(--button-text); display: flex; align-items: center; justify-content: center; }

  .divider { position: absolute; left: 0; top: 413px; width: 754px; height: 32px; z-index: 1; }

  .fresh-band { position: absolute; left: 0; top: 425px; width: 754px; height: 88px; background: linear-gradient(#2b2b2b, #343434); }
  .fresh-title { position: absolute; left: 80px; top: 444px; font-family: "Arvo", serif; font-weight: 700; font-size: 31px; color: var(--white); z-index: 2; }

  .collections { position: absolute; left: 0; top: 513px; width: 754px; height: 520px; background: radial-gradient(ellipse at 50% 40%, var(--chalk-mid), var(--chalk-dark) 80%); }
  .card { position: absolute; width: 149px; height: 202px; }
  .card-photo { width: 149px; height: 147px; }
  .card-caption { height: 55px; background: var(--card-caption); padding: 9px 10px; font-family: "Arvo", serif; font-size: 16px; line-height: 19px; color: var(--card-text); }

  .site-footer { position: absolute; left: 0; top: 1033px; width: 754px; height: 167px; background: var(--white); font-family: "Anonymous Pro", monospace; font-size: 10px; line-height: 12px; color: var(--footer-text); }
  .footer-col { position: absolute; top: 14px; }
  .footer-heading { margin-bottom: 13px; }
  .newsletter-form { display: flex; margin-top: 12px; }
  .email-field { width: 125px; height: 20px; background: var(--input-bg); padding: 4px 6px; }
  .signup-button { width: 54px; height: 20px; background: var(--signup-red); color: var(--white); display: flex; align-items: center; justify-content: center; }
  .copyright { position: absolute; top: 137px; left: 0; width: 754px; text-align: center; }
</style>
</head>
<body>
<div class="page">
  <header class="site-header">
    <nav class="nav nav-left"><span>HOME</span><span>SHOP</span></nav>
    <nav class="nav nav-right"><span>CURATED</span><span>ABOUT US</span></nav>
  </header>
  <div class="brand"><span class="brand-name">BRISA</span><span class="brand-dot"></span><span class="brand-name">PETALS</span></div>

  <section class="hero">
    <div class="hero-photo" role="img" aria-label="Photo of red and pink roses among dark green leaves"></div>
    <div class="hero-emblem" role="img" aria-label="Decorative floral emblem"></div>
    <h1 class="hero-title"><span class="bold">COSTA</span><span class="thin">SOL.</span></h1>
    <p class="hero-tagline">spring collection</p>
    <a class="hero-button">VIEW NOW.</a>
  </section>

  <svg class="divider" viewBox="0 0 754 32" aria-hidden="true">
    <rect x="0" y="0" width="754" height="12" fill="#ffffff"/>
    <polygon points="366,12 424,12 395,32" fill="#ffffff"/>
  </svg>

  <div class="fresh-band"></div>
  <h2 class="fresh-title">Fresh this week</h2>

  <section class="collections">
    <article class="card" style="left:99px; top:16px;">
      <div class="card-photo" role="img" aria-label="Photo of pink and white lilies on wood" style="background:linear-gradient(160deg,#e6c6d6,#6f8a5a 60%,#5b5346);"></div>
      <div class="card-caption">Any Occasion<br>2 products</div>
    </article>
    <article class="card" style="left:303px; top:16px;">
      <div class="card-photo" role="img" aria-label="Photo of pink gerbera bouquet in kraft paper" style="background:radial-gradient(circle at 50% 40%,#e84f83,#c29a74 45%,#8a7b6c);"></div>
      <div class="card-caption">Birthday<br>1 product</div>
    </article>
    <article class="card" style="left:503px; top:16px;">
      <div class="card-photo" role="img" aria-label="Photo of white calla lilies on dark wood" style="background:linear-gradient(140deg,#f1f1ee,#7f8b6a 50%,#3f3f40);"></div>
      <div class="card-caption">Dude<br>1 product</div>
    </article>
    <article class="card" style="left:99px; top:270px;">
      <div class="card-photo" role="img" aria-label="Photo of a bundle of red roses" style="background:radial-gradient(circle at 45% 40%,#a81e2c,#6b1019 60%,#6e6a62);"></div>
      <div class="card-caption">Love<br>1 product</div>
    </article>
    <article class="card" style="left:303px; top:270px;">
      <div class="card-photo" role="img" aria-label="Photo of orange and yellow lilies wrapped in paper" style="background:radial-gradient(circle at 50% 45%,#f07a3a,#e7c24a 40%,#9a948a);"></div>
      <div class="card-caption">Thank you<br>1 product</div>
    </article>
  </section>

  <footer class="site-footer">
    <div class="footer-col" style="left:33px;">
      <p class="footer-heading">Meet Brisa &gt;</p>
      <p>Based in Palmwood, San Diego<br>We offer farm fresh, curated,<br>cool, and same day delivery flower bouquets.<br>ChirperFacepageSnapgram</p>
    </div>
    <div class="footer-col" style="left:317px;">
      <p class="footer-heading">Reach Brisa &gt;</p>
      <p>2218 Palmera Avenue<br>San Diego, CA 92199<br>Email: info@brisapetals.example<br>Phone: 619-555-0147</p>
    </div>
    <div class="footer-col" style="left:542px;">
      <p class="footer-heading">Newsletter &gt;</p>
      <p>We promise to only send you good<br>things like discounts!</p>
      <form class="newsletter-form"><span class="email-field">Your Email</span><span class="signup-button">Sign up</span></form>
    </div>
    <p class="copyright">Copyright © 2014 brisapetals of San Diego. Website builder by Quartzcart.</p>
  </footer>
</div>
</body>
</html>
```